The Copper Tides (celtic rap album by Rudi Van Oske)

Peace. I'm Rudi Van Oske, I make celtic/druidic/pagan rap music. The album is called ' The Copper Tides ' which has to do with celtic cosmology: The Underworld (The Sea) is the realms of the past, the ancestors, trauma, transformation, knowledge of the old ways ... ; This World (The Land) is the realm of ordinary reality, our life, the present, skills, fertility ... ; and The Upperworld (The Sky) which is the realm of the gods, the future, goals, planning of harvest.... Three was a sacred number and describes the fullness of life and is symbolized by the triskele, e.g. found at Calderwick.

I have no idea for a cover lol, so go wild. It would be good if the three worlds are somehow featured.

This is one of the songs: https://www.vidharbor.net/watch?v=qTr8LmZxW2p

Target Market(s)

pagans, spiritual people

Requirements
Must have
• something that references The Copper Tides (see description)
Nice to have
• Celtic symbol(s); contrasts between light and dark; past - present - future

```html
<!DOCTYPE html>
<html lang="en">
<head>
<meta charset="utf-8">
<title>The Copper Tides – Rudi Van Oske</title>
<link rel="stylesheet" href="https://fonts.googleapis.com/css2?family=Staatliches&display=swap">
<style>
  :root {
    --paper: #ffffff;
    --ink: #1c1c1c;
    --knot-dark: #161616;
    --sky: #4a63c9;
    --sky-light: #9d9fd6;
    --sea: #2fb3b0;
    --land: #d9a55c;
  }
  html, body {
    margin: 0;
    padding: 0;
    overflow: hidden;
    background: var(--paper);
  }
  .album-cover {
    position: relative;
    width: 1200px;
    height: 1200px;
    background: var(--paper);
    overflow: hidden;
  }
  .realms-emblem {
    position: absolute;
    left: 190px;
    top: 100px;
    width: 840px;
    height: 830px;
    border-radius: 50%;
    background:
      radial-gradient(circle at 50% 28%, var(--sky-light) 0%, var(--sky) 16%, transparent 30%),
      radial-gradient(circle at 30% 66%, var(--sea) 0%, transparent 24%),
      radial-gradient(circle at 70% 66%, var(--land) 0%, transparent 24%),
      radial-gradient(circle at 50% 50%, #3a3a3a 0%, var(--knot-dark) 70%);
  }
  .album-title {
    position: absolute;
    left: 0;
    right: 0;
    top: 972px;
    margin: 0;
    text-align: center;
    font-family: "Staatliches", sans-serif;
    font-weight: 400;
    font-size: 86px;
    line-height: 1;
    letter-spacing: 0.1em;
    color: var(--ink);
  }
  .artist-name {
    position: absolute;
    left: 0;
    right: 0;
    top: 1090px;
    margin: 0;
    text-align: center;
    font-family: "Staatliches", sans-serif;
    font-weight: 400;
    font-size: 44px;
    line-height: 1;
    letter-spacing: 0.08em;
    color: var(--ink);
  }
</style>
</head>
<body>
  <main class="album-cover">
    <div class="realms-emblem" role="img" aria-label="Sketched Celtic trinity knot within a circle, its three lobes filled with spirals in sky blue, sea teal and land ochre, representing the Upperworld, the Underworld and This World"></div>
    <h1 class="album-title">The Copper Tides</h1>
    <p class="artist-name">Rudi Van Oske</p>
  </main>
</body>
</html>
```